Consulting Company Business Card

I am looking for a minimalist, classy, professional design on my business card. I would like it to be double-sided. I want to use the font and color scheme of my logo which are attached. Please be creative in the designs that you send me. I want to play off the design of my logo with the inner C that is Green and Blue broken up with the white.
Target Market(s)
Small Businesses
Industry/Entity Type
Consulting
Contact Information for Business Card
Dale M. Whitcombe, CPA CGMA, 555-014-2873, dwhitcombe@vorantaadvisory.example, www.vorantaadvisory.example

```html
<!DOCTYPE html>
<html lang="en">
<head>
<meta charset="utf-8">
<title>Voranta Advisory – Business Card</title>
<link rel="stylesheet" href="https://fonts.googleapis.com/css2?family=Jost:wght@400;600&family=Open+Sans:wght@400&display=swap">
<style>
  :root {
    --stage: #b9b9bb;
    --navy: #1c2f5a;
    --navy-deep: #172849;
    --teal: #2e9a93;
    --paper: #ffffff;
    --ink-soft: #4a4d55;
    --icon: #3a3d44;
  }
  * { box-sizing: border-box; margin: 0; padding: 0; }
  html, body { width: 1200px; height: 876px; overflow: hidden; }
  body {
    background: var(--stage);
    position: relative;
    font-family: "Jost", "Helvetica Neue", Arial, sans-serif;
  }
  .card {
    position: absolute;
    width: 600px;
    height: 343px;
    border-radius: 4px;
    box-shadow: 0 10px 28px rgba(0,0,0,0.25);
    overflow: hidden;
  }

  /* Back side */
  .card-back {
    left: 520px;
    top: 80px;
    background: linear-gradient(135deg, var(--navy) 0%, var(--navy-deep) 100%);
    display: flex;
    align-items: center;
    justify-content: center;
  }
  .wordmark {
    display: flex;
    flex-direction: column;
    align-items: center;
    font-weight: 600;
    text-transform: uppercase;
    line-height: 1;
  }
  .card-back .wordmark { color: var(--paper); }
  .card-back .wordmark-main { font-size: 62px; letter-spacing: 1px; }
  .card-back .wordmark-sub { font-size: 20px; letter-spacing: 9px; margin-top: 8px; }

  /* Front side */
  .card-front {
    left: 90px;
    top: 450px;
    background: var(--paper);
    display: flex;
  }
  .front-band {
    width: 150px;
    height: 100%;
    background: linear-gradient(160deg, var(--navy) 0%, var(--navy-deep) 100%);
  }
  .front-body {
    flex: 1;
    padding: 30px 34px 0 40px;
  }
  .brand {
    display: flex;
    align-items: center;
    gap: 12px;
    margin-left: 60px;
  }
  .brand-dot {
    width: 34px;
    height: 34px;
    border-radius: 50%;
    background: var(--teal);
    flex: none;
  }
  .card-front .wordmark { color: var(--navy); align-items: flex-start; }
  .card-front .wordmark-main { font-size: 40px; letter-spacing: 0.5px; }
  .card-front .wordmark-sub { font-size: 13px; letter-spacing: 7px; margin-top: 4px; }

  .holder-name {
    margin-top: 26px;
    font-weight: 400;
    font-size: 31px;
    letter-spacing: 1.5px;
    color: var(--navy);
    text-transform: uppercase;
    white-space: nowrap;
  }
  .contact-list {
    list-style: none;
    margin-top: 16px;
    font-family: "Open Sans", Arial, sans-serif;
    font-size: 15px;
    color: var(--ink-soft);
  }
  .contact-item {
    display: flex;
    align-items: center;
    gap: 10px;
    height: 28px;
  }
  .contact-phone { margin-left: 86px; }
  .contact-icon { width: 20px; height: 20px; flex: none; }
</style>
</head>
<body>

  <section class="card card-back" aria-label="Business card back">
    <div class="wordmark">
      <span class="wordmark-main">Voranta</span>
      <span class="wordmark-sub">Advisory</span>
    </div>
  </section>

  <section class="card card-front" aria-label="Business card front">
    <div class="front-band"></div>
    <div class="front-body">
      <div class="brand">
        <span class="brand-dot"></span>
        <div class="wordmark">
          <span class="wordmark-main">Voranta</span>
          <span class="wordmark-sub">Advisory</span>
        </div>
      </div>

      <h1 class="holder-name">Dale M. Whitcombe</h1>

      <ul class="contact-list">
        <li class="contact-item contact-phone">
          <svg class="contact-icon" viewBox="0 0 20 20" aria-hidden="true">
            <circle cx="10" cy="10" r="9" fill="none" stroke="var(--icon)" stroke-width="1.5"/>
            <path d="M7 5.5c-.8.5-1.3 1.3-1 2.5.6 2.5 2.7 4.8 5.2 5.7 1.1.4 2 0 2.6-.8l-1.6-1.6-1.2.6c-1-.5-2-1.5-2.5-2.5l.6-1.2L7 5.5z" fill="var(--icon)"/>
          </svg>
          <span>555-014-2873</span>
        </li>
        <li class="contact-item">
          <svg class="contact-icon" viewBox="0 0 20 20" aria-hidden="true">
            <circle cx="10" cy="10" r="9.5" fill="var(--icon)"/>
            <rect x="5" y="6.5" width="10" height="7" fill="none" stroke="#fff" stroke-width="1.2"/>
            <path d="M5 6.5l5 4 5-4" fill="none" stroke="#fff" stroke-width="1.2"/>
          </svg>
          <span>dwhitcombe@vorantaadvisory.example</span>
        </li>
        <li class="contact-item">
          <svg class="contact-icon" viewBox="0 0 20 20" aria-hidden="true">
            <circle cx="10" cy="10" r="9.5" fill="var(--icon)"/>
            <circle cx="10" cy="10" r="5.5" fill="none" stroke="#fff" stroke-width="1.1"/>
            <ellipse cx="10" cy="10" rx="2.3" ry="5.5" fill="none" stroke="#fff" stroke-width="1.1"/>
            <path d="M4.5 10h11" stroke="#fff" stroke-width="1.1"/>
          </svg>
          <span>www.vorantaadvisory.example</span>
        </li>
      </ul>
    </div>
  </section>

</body>
</html>
```